International Property Consultancy

Brief Overview:

I need a dynamic and well designed website that is easy to use and understand. It has to be unique and different to generic templates that most websites seem to be these days. PLEASE NO GENERIC TEMPLATES FROM THE INTERNET.

Our business has 10 years experience working on struggling international developments that we then work in-house for to turn around and brings bout success. We stay within a project often for long periods of time until success is achieved. We are unique in our approach and completely different to the standard routes to market for many developments. The site is for developers to see what we have done in regards to previous projects, as such we want to incorporate video into this site with a strong design aesthetic. There will be videos of the past projects we have worked on, which will act as case studies.

I like very simple but punchy websites, that people can navigate and understand very easily. Also a big fan of unique and well thought out design aesthetic.

Initial Site layout thoughts:

1) Homepage:
2) About Us
3) What we've done / Work
This part has the projects we have worked on (France, Portugal, London, Morocco). Each one will have some video content and photo images, but also would be good to have a succinct way to mention what we did and the successes in a clever and punchy way.

4) Contact Us

* This is just a guideline. Would be open to input and creative direction on your own part.

*More details and websites we like can be seen in the brief doc attached.

PLEASE VIEW THE WIREFRAME WORD DOC ATTACHED.

Here there are also some more examples to help:

Here are just a few examples of websites and what I like about them:

- www.velmoro.com (clean, nice geometric design aesthetic, good animation when loading and changing pages well thought out all though also coulee be considered a bit dull and basic after the initial homepage slide)
- https://www.farbridgehub.net (Clean site, quite clinical, lacks video content and doesn't engage greatly).
- https://ruskotile.com (minimal, and like how it mixes the design aesthetic more with video and photo content)

- https://www.amberquillworks.com (like the layout of this and how it displays the projects and work section)

- https://brisk.com (Good use of video content)

- https://loomfield.studio (minimal to the point and mixes design with video and animation etc...)

Here is another couple of cool websites that may help give you some direction: https://halvenquay.com www.brisk.com

Hi there, One of the things I thought would be good on the homepage is to add the logo with a 'digital landscape' before flicking down into a slide with video content of the projects... Just an idea but have posted some pics in the brief. We would get this animated for the site. But if you have better ideas, please do run with them. Thanks,

Target Market(s)

Property developers

Number of Pages Required

4 page

Font styles to use
Other font styles liked:
• Read brief

Requirements
Must have
• Needs to be clean, dynamic and easy to follow on desktop and mobile. We will use it as a kind of portfolio website so will need to embed video of past projects we have worked on.

Read brief in docs.
Nice to have
• Clean
Should not have
• Not be another generic template website.
Not have random property stock photos. (We are not a property agency).

```html
<!DOCTYPE html>
<html lang="en">
<head>
<meta charset="utf-8">
<title>Calvenor — International Property Developments</title>
<link href="https://fonts.googleapis.com/css2?family=Barlow+Condensed:wght@500&family=Montserrat:wght@400;500;600;700&display=swap" rel="stylesheet">
<style>
:root{
  --ink:#13171c;
  --teal:#0f3d4f;
  --blush:#f8e1da;
  --blush-deep:#f6ddd5;
  --orange:#ff5722;
  --blue:#1a5ea8;
  --grey:#5b5f66;
  --footer:#f4f4f4;
  --white:#ffffff;
}
*{margin:0;padding:0;box-sizing:border-box}
html,body{width:732px;height:1200px;overflow:hidden;background:var(--white)}
body{position:relative;font-family:"Montserrat",sans-serif;color:var(--ink)}
.abs{position:absolute}

.site-header .brand{left:60px;top:9px;font-size:16px;font-weight:600;letter-spacing:-.2px;color:var(--ink)}
.menu-toggle{left:656px;top:11px;width:17px;height:13px}
.menu-toggle span{position:absolute;right:0;height:2px;background:var(--blue);border-radius:1px}

.hero-art{left:348px;top:71px;width:34px;height:42px;border-radius:3px;background:linear-gradient(180deg,#fde3d8,#fbd2c2)}
.corner-art{left:688px;top:70px;width:44px;height:42px;border-radius:3px;background:linear-gradient(180deg,#fbe8e1,#f6e3de)}
.side-art{left:2px;top:138px;width:36px;height:36px;border-radius:3px;background:#eef2f4}

.eyebrow{left:0;width:732px;top:124px;text-align:center;font-size:12.5px;font-weight:500;letter-spacing:6px}
.hero-title{left:0;width:732px;top:146px;text-align:center;font-size:37px;font-weight:700;line-height:41px;letter-spacing:.2px}

.intro-band{left:0;top:371px;width:732px;height:280px;background:var(--blush)}
.intro-band .deco{left:314px;top:74px;width:104px;height:34px;border-radius:3px;background:rgba(35,31,32,.05)}
.intro-band .brand{left:0;width:732px;top:104px;text-align:center;font-size:46px;font-weight:600;letter-spacing:-.5px;color:#231f20}
.intro-band .tagline{left:0;width:732px;top:158px;text-align:center;font-size:9.8px;font-weight:500;color:#4a4648}
.play-btn{left:61px;top:191px;width:58px;height:58px;border-radius:50%;background:var(--white);box-shadow:0 6px 16px rgba(0,0,0,.08)}
.play-btn svg{position:absolute;left:26px;top:25px}

.success .count{left:60px;top:786px;font-family:"Barlow Condensed",sans-serif;font-size:68px;font-weight:500;line-height:60px;color:var(--blush-deep)}
.success h2{left:122px;top:795px;font-size:22.5px;font-weight:700;line-height:23px;color:var(--teal)}
.success p{left:72px;top:861px;width:300px;font-size:11px;line-height:16px;color:var(--grey)}
.btn{left:77px;top:913px;width:121px;height:31px;background:var(--orange);color:var(--white);font-size:10.5px;font-weight:500;line-height:31px;text-align:center;text-decoration:none}
.success .visual{left:426px;top:706px;width:306px;height:294px;border-radius:6px;background:linear-gradient(160deg,#eef1fa 0%,#d5dbf1 50%,#8f8ac4 100%)}

.site-footer{left:0;top:1071px;width:732px;height:129px;background:var(--footer)}
.site-footer .brand{left:0;width:732px;top:35px;text-align:center;font-size:15px;font-weight:600;color:var(--ink)}
.footer-nav{left:0;width:732px;top:67px;text-align:center;font-size:8.4px;color:var(--grey)}
.footer-nav a{color:inherit;text-decoration:none}
.footer-nav .sep{margin:0 10px}
.rule{left:60px;top:101px;width:612px;height:1px;background:#dcdcdc}
.copyright{left:60px;top:107px;font-size:7.4px;color:var(--grey)}
.social{left:598px;top:106px;display:flex;gap:9.5px}
.social a{display:block;width:11px;height:11px;border-radius:50%;background:var(--blue)}
</style>
</head>
<body>
<header class="site-header">
  <div class="brand abs">calvenor.</div>
  <div class="menu-toggle abs" aria-label="Menu">
    <span style="top:0;width:12px"></span>
    <span style="top:5px;width:17px"></span>
    <span style="top:10px;width:14px"></span>
  </div>
</header>

<div class="hero-art abs" role="img" aria-label="Small idea illustration"></div>
<div class="corner-art abs" role="img" aria-label="Small goal illustration"></div>
<div class="side-art abs" role="img" aria-label="Small hand-drawn scribble"></div>

<p class="eyebrow abs">WE ARE CALVENOR</p>
<h1 class="hero-title abs">We Fulfill International<br>Property Developments</h1>

<section class="intro-band abs">
  <div class="deco abs" role="img" aria-label="Hand-drawn scribble line"></div>
  <div class="brand abs">calvenor.</div>
  <p class="tagline abs">FINDING PROPERTY BUSINESS SOLUTIONS</p>
  <div class="play-btn abs" aria-label="Play video">
    <svg width="8" height="9" viewBox="0 0 8 9"><path d="M0 0L7 4.5L0 9Z" fill="#111"/></svg>
  </div>
</section>

<section class="success">
  <div class="count abs">10</div>
  <h2 class="abs">YEARS OF SUCCESS<br>AROUND THE WORLD</h2>
  <p class="abs">We deliver a unique and truly bespoke approach to delivering international developments to market</p>
  <a class="btn abs" href="#">SEE OUR WORK</a>
  <div class="visual abs" role="img" aria-label="Illustration of a presentation easel with a bar chart"></div>
</section>

<footer class="site-footer abs">
  <div class="brand abs">calvenor.</div>
  <nav class="footer-nav abs">
    <a href="#">HOME</a><span class="sep">I</span><a href="#">ABOUT US</a><span class="sep">I</span><a href="#">OUR WORK</a><span class="sep">I</span><a href="#">CONTACFT US</a>
  </nav>
  <div class="rule abs"></div>
  <p class="copyright abs">COPYRIGHT © 2020 COMPANY ALL RIGHTS RESERVED.</p>
  <div class="social abs">
    <a href="#" aria-label="Social profile 1"></a>
    <a href="#" aria-label="Social profile 2"></a>
    <a href="#" aria-label="Social profile 3"></a>
    <a href="#" aria-label="Social profile 4"></a>
  </div>
</footer>
</body>
</html>
```